Accounting business needs business card

I have a business card but need something better. I want the colour changed and the design to be better. I have uploaded a picture of my new sign that is grey in colour, i would like to incorporate these colours.

```html
<!DOCTYPE html>
<html lang="en">
<head>
<meta charset="UTF-8">
<title>Nil Ledger – Business Card</title>
<link rel="stylesheet" href="https://fonts.googleapis.com/css2?family=Montserrat:wght@400;500;600&display=swap">
<style>
  :root {
    --stage: #2b2b2b;
    --card-dark: #141414;
    --card-dark-2: #222222;
    --card-light: #ffffff;
    --ink: #1f1f1f;
    --ink-soft: #6e6e6e;
    --rule: #6a6a6a;
    --icon: #8a8a8a;
    --badge-fill: #d4d4d4;
    --badge-mid: #a8a8a8;
  }
  * { box-sizing: border-box; margin: 0; padding: 0; }
  html, body { width: 1200px; height: 900px; overflow: hidden; }
  body {
    background: var(--stage);
    font-family: "Montserrat", sans-serif;
    position: relative;
  }
  .card {
    position: absolute;
    left: 250px;
    width: 700px;
    height: 400px;
    box-shadow: 0 10px 30px rgba(0,0,0,.45);
  }
  /* back side */
  .card-back {
    top: 35px;
    background: var(--card-dark);
    overflow: hidden;
  }
  .card-back .pattern {
    position: absolute;
    inset: 0;
    background: linear-gradient(150deg, var(--card-dark-2) 0%, var(--card-dark) 70%);
  }
  .card-back .wordmark {
    position: absolute;
    right: 60px;
    bottom: 60px;
    color: #fff;
    font-size: 30px;
    font-weight: 500;
    letter-spacing: 0.42em;
  }
  /* front side */
  .card-front {
    top: 465px;
    background: var(--card-light);
    color: var(--ink);
  }
  .brand {
    position: absolute;
    left: 40px;
    top: 38px;
    display: flex;
    align-items: center;
    gap: 22px;
  }
  .brand-dot {
    width: 62px; height: 62px;
    border: 2px solid var(--ink);
    border-radius: 50%;
  }
  .brand-name {
    font-size: 22px;
    font-weight: 500;
    letter-spacing: 0.42em;
  }
  .divider {
    position: absolute;
    left: 40px;
    top: 178px;
    width: 370px;
    height: 2px;
    background: var(--rule);
  }
  .contacts {
    position: absolute;
    left: 40px;
    top: 222px;
    list-style: none;
    font-size: 20px;
    line-height: 34px;
  }
  .contacts li { display: flex; align-items: center; gap: 14px; }
  .contacts svg { width: 20px; height: 20px; fill: var(--icon); flex: none; }
  .person {
    position: absolute;
    right: 40px;
    top: 200px;
    text-align: right;
  }
  .person-name {
    font-size: 22px;
    font-weight: 600;
    letter-spacing: 0.02em;
  }
  .person-creds, .person-role {
    font-size: 15px;
    color: var(--ink-soft);
    line-height: 22px;
  }
  .badges {
    position: absolute;
    right: 40px;
    bottom: 36px;
    display: flex;
    align-items: center;
    gap: 16px;
  }
  .badge-membership {
    width: 136px; height: 56px;
    background: var(--badge-fill);
  }
  .badge-software {
    width: 64px; height: 64px;
    border-radius: 50%;
    background: var(--badge-mid);
  }
  .badge-registered {
    width: 58px; height: 58px;
    border-radius: 50%;
    border: 3px solid var(--ink);
    background: #fff;
  }
</style>
</head>
<body>

<section class="card card-back">
  <div class="pattern" role="img" aria-label="Repeating tone-on-tone pattern of the brand monogram"></div>
  <div class="wordmark">NIL LEDGER</div>
</section>

<section class="card card-front">
  <div class="brand">
    <span class="brand-dot"></span>
    <span class="brand-name">NIL LEDGER</span>
  </div>

  <div class="divider"></div>

  <ul class="contacts">
    <li>
      <svg viewBox="0 0 24 24" aria-hidden="true"><path d="M6.6 10.8a15.1 15.1 0 0 0 6.6 6.6l2.2-2.2a1 1 0 0 1 1-.25 11.4 11.4 0 0 0 3.6.57 1 1 0 0 1 1 1V20a1 1 0 0 1-1 1A17 17 0 0 1 3 4a1 1 0 0 1 1-1h3.5a1 1 0 0 1 1 1c0 1.25.2 2.45.57 3.6a1 1 0 0 1-.25 1z"/></svg>
      <span>0400 218 365</span>
    </li>
    <li>
      <svg viewBox="0 0 24 24" aria-hidden="true"><path d="M3 5h18a1 1 0 0 1 1 1v.4l-10 7-10-7V6a1 1 0 0 1 1-1zm-1 3.8 10 7 10-7V18a1 1 0 0 1-1 1H3a1 1 0 0 1-1-1z"/></svg>
      <span>dean@nilledger.com.au</span>
    </li>
    <li>
      <svg viewBox="0 0 24 24" aria-hidden="true"><path d="M12 2a10 10 0 1 0 0 20 10 10 0 0 0 0-20zm-1 17.9A8 8 0 0 1 4.1 10H7l2 2v1l2 2zm6.9-2.5A2 2 0 0 0 16 16h-1v-3a1 1 0 0 0-1-1H8v-2h2a1 1 0 0 0 1-1V7h2a2 2 0 0 0 2-2v-.4a8 8 0 0 1 2.9 12.8z"/></svg>
      <span>www.nilledger.com.au</span>
    </li>
  </ul>

  <div class="person">
    <p class="person-name">DEAN HALLOWAY</p>
    <p class="person-creds">CPA, MTAX, BCOM (Acc &amp; Fin)</p>
    <p class="person-role">Taxation &amp; Business Accountant</p>
  </div>

  <div class="badges">
    <div class="badge-membership" role="img" aria-label="Professional membership badge"></div>
    <div class="badge-software" role="img" aria-label="Accounting software partner badge"></div>
    <div class="badge-registered" role="img" aria-label="Registered tax agent badge"></div>
  </div>
</section>

</body>
</html>
```